Design a New Business Card for Our Company

We are looking for fresh, unique, and a modern business card that reflects our roots as digital marketing agency focused on SEM.

Industry/Entity Type

Marketing

Contact Information for Business Card

looking for very unique out of the box designs. clean and modern that compliments our logo

Requirements
Must have
• colors should match our logo
• Front should have name, address, email, and phone/fax of the person, phone/fax are the same number
• back should have our url

```html
<!DOCTYPE html>
<html lang="en">
<head>
<meta charset="utf-8">
<title>Brightwave Partners – Business Card</title>
<link href="https://fonts.googleapis.com/css2?family=Open+Sans:wght@400;600;700&display=swap" rel="stylesheet">
<style>
  :root {
    --brand-blue: #5390cf;
    --brand-blue-dark: #3f7cc0;
    --soft-blue: #dde6f1;
    --paper: #f6f7f8;
    --ink: #3d3d3d;
    --grey: #8a8a8a;
    --rule: #c9c9c9;
    --backdrop: #e9e7e5;
  }
  * { margin: 0; padding: 0; box-sizing: border-box; }
  html, body { width: 1200px; height: 942px; overflow: hidden; }
  body {
    background: var(--backdrop);
    font-family: "Open Sans", Arial, sans-serif;
    position: relative;
  }
  .card {
    position: absolute;
    width: 630px;
    height: 360px;
    border-radius: 4px;
    overflow: hidden;
    box-shadow: 0 6px 18px rgba(0,0,0,0.15);
  }
  /* Back of card */
  .card--back {
    left: 60px; top: 60px;
    background: var(--brand-blue);
  }
  .card--back .decor {
    position: absolute; right: 0; top: 0;
    width: 300px; height: 260px;
    background: radial-gradient(ellipse at 60% 45%, rgba(255,255,255,0.22), rgba(255,255,255,0) 70%);
  }
  .card--back .wordmark {
    position: absolute; left: 70px; top: 140px;
    display: flex; align-items: center; gap: 16px;
    color: #ffffff;
  }
  .wordmark .mark-dot {
    width: 34px; height: 34px; border-radius: 50%;
    background: currentColor;
  }
  .wordmark .name {
    font-weight: 700; font-size: 52px; letter-spacing: -1px; line-height: 1;
  }
  .card--back .url {
    position: absolute; right: 70px; bottom: 40px;
    color: #ffffff; font-size: 15px;
  }
  /* Front of card */
  .card--front {
    left: 510px; top: 520px;
    background: var(--paper);
  }
  .card--front .decor {
    position: absolute; right: 20px; top: 10px;
    width: 270px; height: 230px;
    background: radial-gradient(ellipse at 55% 45%, var(--soft-blue), rgba(221,230,241,0) 70%);
  }
  .card--front .wordmark {
    position: absolute; left: 40px; top: 90px;
    color: var(--brand-blue);
    gap: 12px;
  }
  .card--front .wordmark .mark-dot { width: 22px; height: 22px; }
  .card--front .wordmark .name { font-size: 34px; }
  .card--front .divider {
    position: absolute; left: 150px; right: 240px; top: 175px;
    border-top: 1px solid var(--rule);
  }
  .person {
    position: absolute; right: 40px; top: 62px; text-align: right;
  }
  .person .full-name {
    color: var(--brand-blue); font-size: 24px; font-weight: 400;
    border-bottom: 1.5px solid var(--brand-blue); padding-bottom: 2px;
  }
  .person .role { color: var(--ink); font-size: 12px; margin-top: 2px; }
  .address {
    position: absolute; right: 40px; top: 150px; text-align: right;
    color: var(--ink); font-size: 13px; line-height: 1.45;
  }
  .contacts {
    position: absolute; left: 60px; top: 200px;
    list-style: none; color: var(--ink); font-size: 14px; line-height: 1.55;
  }
  .contacts li { display: flex; align-items: center; gap: 8px; }
  .contacts svg { width: 13px; height: 13px; fill: var(--brand-blue); }
  .card--front .wave { position: absolute; left: 0; bottom: 0; width: 630px; height: 130px; }
  .card--front .url {
    position: absolute; right: 70px; bottom: 42px;
    color: #ffffff; font-size: 13px; transform: rotate(-9deg);
  }
</style>
</head>
<body>
  <section class="card card--back" aria-label="Business card back">
    <div class="decor" role="img" aria-label="Soft pale blue bubble pattern"></div>
    <div class="wordmark">
      <span class="mark-dot"></span>
      <span class="name">brightwave</span>
    </div>
    <div class="url">www.brightwavepartners.com</div>
  </section>

  <section class="card card--front" aria-label="Business card front">
    <div class="decor" role="img" aria-label="Soft pale blue bubble pattern"></div>
    <div class="wordmark">
      <span class="mark-dot"></span>
      <span class="name">brightwave</span>
    </div>
    <div class="divider"></div>
    <div class="person">
      <div class="full-name">Daniel Hartley</div>
      <div class="role">President</div>
    </div>
    <div class="address">418 Maple Ridge Rd<br>Glendale, CA 91208 USA</div>
    <ul class="contacts">
      <li><svg viewBox="0 0 16 16"><path d="M3 1l3 3-2 2c1 2 3 4 5 5l2-2 3 3-2 3C6 15 1 10 1 3z"/></svg>555-014-2290</li>
      <li><svg viewBox="0 0 16 16"><rect x="4" y="1" width="8" height="5"/><rect x="1" y="6" width="14" height="9" rx="1"/></svg>555-014-2290</li>
      <li><svg viewBox="0 0 16 16"><path d="M1 3h14v10H1z M1 3l7 6 7-6" /></svg>hello@examplemail.com</li>
    </ul>
    <svg class="wave" viewBox="0 0 630 130" preserveAspectRatio="none" aria-hidden="true">
      <path d="M0 95 C180 80 380 40 630 0 L630 10 C380 50 180 95 0 108 Z" fill="#bdbdbd"/>
      <path d="M0 112 C200 98 400 55 630 18 L630 130 L0 130 Z" fill="var(--brand-blue)"/>
    </svg>
    <div class="url">www.brightwavepartners.com</div>
  </section>
</body>
</html>
```